Business card design needed

Business Card design required for new small plumbing business.
Would like a logo/text look that is simple and unique and does not have to be representative of a plumbing company (ie. having a cartoon plumber or toilet etc) as the companyname is self explanatory.
Would like the main colour to be green (lime green).
Updates

Industry/Entity Type

Plumber

Contact Information for Business Card

BRAVELL PLUMBING
ABN 61 904 127 558 003

Trevor Hasketh
Licensed Plumber 83615
Phone: 0412 870 245

27 Bravell Drive,
Thornbank. 4826 Eastmere

Email: bravellplumbing@mailnest.example

Logo Text

Bravell Plumbing

Logo styles of interest
Character Logo
Wordmark Logo
Lettermark Logo

```html
<!DOCTYPE html>
<html lang="en">
<head>
<meta charset="utf-8">
<title>Bravell Plumbing – Business Card</title>
<link rel="stylesheet" href="https://fonts.googleapis.com/css2?family=Tinos:wght@400;700&display=swap">
<style>
  :root {
    --card-green: #b3ff8a;
    --ink: #000000;
    --highlight: #ffffff;
  }
  html, body {
    margin: 0;
    padding: 0;
    overflow: hidden;
  }
  .card {
    position: relative;
    width: 1200px;
    height: 741px;
    background: var(--card-green);
    font-family: "Tinos", "Times New Roman", serif;
    color: var(--ink);
    overflow: hidden;
  }
  .card-line {
    position: absolute;
    right: 22px;
    margin: 0;
    white-space: nowrap;
    line-height: 1;
    font-weight: 700;
    text-shadow: -2px 2px 0 var(--highlight);
    transform-origin: right top;
  }
  .business-name {
    top: 20px;
    font-size: 76px;
    font-weight: 400;
    letter-spacing: 0.14em;
    margin-right: -11px;
    -webkit-text-stroke: 1px var(--ink);
  }
  .holder-title {
    top: 137px;
    font-size: 54px;
    transform: scaleX(0.8);
  }
  .contact-phone {
    top: 510px;
    right: 33px;
    font-size: 54px;
    transform: scaleX(0.8);
  }
  .contact-address {
    top: 591px;
    right: 38px;
    font-size: 54px;
    transform: scaleX(0.8);
  }
  .contact-email {
    top: 661px;
    font-size: 54px;
    transform: scaleX(0.74);
  }
</style>
</head>
<body>
  <main class="card">
    <h1 class="card-line business-name">BRAVELL PLUMBING ABN</h1>
    <p class="card-line holder-title">TREVOR HASKETH LICENSED PLUMBER</p>
    <p class="card-line contact-phone">PHONE: 0412 870 245</p>
    <p class="card-line contact-address">27 BRAVELL DRIVE, THORNBANK. 4826 EASTMERE</p>
    <p class="card-line contact-email">EMAIL: BRAVELLPLUMBING@MAILNEST.EXAMPLE</p>
  </main>
</body>
</html>
```